Web Design Project

We need web design for a new baby products (nursery furniture) business in Australia.

The logo is already done, and I would like to reflect a similar theme throughout the website:
* Clean, white background.
* Use of lime green, purple and orange.
* Similar font to logo for headings
* FUNKY, FASHIONABLE, QUALITY feeling of website.

The main concept is to be attractive to discerning mums who are buying big items like a cot or chest of drawers. These are expensive items and will be considered the most important purchases for a newborn, so the website has to be enticing!!!
Updates

Hello,

Thank you for your submissions. I have received a few questions regarding the font and the coding of this website.

The job I am seeking is for design for an E-commerce store. The font was done by another craft hive designer, so I do not know what type of font I am sorry.

I was hoping to have more designs by now, so please send them soon, this project is guaranteed!

I also ask you to read the brief properly please. The name of the business is Cradle Lane, as the logo says. The use of design that I have mentioned has only been demonstrated in a couple of designs submitted to me.

I look forward to seeing your work soon!

Kind Regards
Marla

Target Market(s)

Young mothers aged 25-45

Industry/Entity Type

Business

Requirements
Must have
• Must be funky, bright, energetic, attractive visually.
Nice to have
• I like the idea of some floral / design work in faded lime green, purple on some of the edges of different pages. Maybe islamic design? But has to be very fashionable.
Should not have
• Should not have any traditional ideas of baby websites.

ie- no stork, nappy images, teddybears etc.

```html
<!DOCTYPE html>
<html lang="en">
<head>
<meta charset="utf-8">
<title>Cradle Lane</title>
<link href="https://fonts.googleapis.com/css2?family=Questrial&display=swap" rel="stylesheet">
<style>
:root{
  --page:#f7f7f3;
  --nav:#dfeeb6;
  --nav-active:#ece07c;
  --nav-text:#5e5c2c;
  --heading:#6a8a1c;
  --body:#7a7a72;
  --muted:#c8bf7c;
  --purple:#b040c8;
  --phone:#cc44cc;
  --panel:#e3efc3;
  --panel-edge:#d6e3b2;
  --field:#d7eaa8;
  --label:#8a8a70;
  --product-bg:#fbe290;
  --tab:#f8b73c;
  --tab-edge:#e9a12a;
  --photo-edge:#f2a23a;
  --dark:#3e3e32;
  --vine:#a9cf4f;
  --vine-light:#d4e98f;
}
*{margin:0;padding:0;box-sizing:border-box}
html,body{width:826px;height:1200px;overflow:hidden;background:var(--page)}
body{font-family:"Questrial",sans-serif;position:relative;color:var(--body)}
.abs{position:absolute}

.social{top:32px;left:690px;display:flex;gap:8px;font-size:9px;color:var(--nav-text)}
.social span{display:flex;align-items:center;gap:3px}
.social i{width:9px;height:9px;background:#5b82c2;display:inline-block}
.social span+span i{background:#8ccbe8}

.brand{top:64px;left:52px;display:flex;align-items:center;gap:10px;font-size:34px;color:var(--purple)}
.brand i{width:34px;height:34px;border-radius:50%;background:#96c81e;display:inline-block}

.nav{top:130px;left:53px;width:574px;height:59px;background:var(--nav);box-shadow:0 1px 2px rgba(0,0,0,.12)}
.nav a{position:absolute;top:0;height:59px;line-height:59px;font-size:13.5px;color:var(--nav-text);text-decoration:none;transform:translateX(-50%);white-space:nowrap}
.nav .active{left:23px;width:107px;transform:none;text-align:center;background:var(--nav-active);box-shadow:0 1px 2px rgba(0,0,0,.15)}

.hero-frame{top:196px;left:38px;width:750px;height:305px;border-radius:10px;background:linear-gradient(90deg,var(--vine-light),var(--vine) 50%,var(--vine-light));padding:7px}
.hero{width:100%;height:100%;border:2px solid #f3f8e2;border-radius:4px;
  background:
    radial-gradient(ellipse 70px 120px at 90px 120px,rgba(232,150,170,.55),transparent 70%),
    radial-gradient(ellipse 110px 150px at 245px 150px,rgba(255,252,240,.95),transparent 72%),
    radial-gradient(ellipse 150px 70px at 390px 230px,rgba(255,250,238,.9),transparent 70%),
    radial-gradient(ellipse 160px 60px at 600px 240px,rgba(252,246,236,.95),transparent 70%),
    radial-gradient(ellipse 60px 80px at 670px 80px,rgba(225,130,160,.45),transparent 70%),
    linear-gradient(180deg,#f1e3dc 0%,#ecd4cc 65%,#e6cabf 100%)}

h2{position:absolute;font-weight:400;font-size:20px;color:var(--heading)}
.welcome-h{top:520px;left:52px}
.welcome-p{top:549px;left:52px;width:452px;font-size:10px;line-height:12.6px;letter-spacing:.55px}
.more{font-size:9px;font-style:italic;color:var(--muted);letter-spacing:.5px}
.welcome-more{top:681px;left:433px}

.products-h{top:709px;left:52px}
.products{top:739px;left:53px;width:447px;height:405px;background:var(--product-bg)}
.tab{position:absolute;top:9px;width:70px;height:34px;line-height:34px;text-align:center;background:var(--tab);border-radius:6px;box-shadow:0 2px 2px var(--tab-edge);color:var(--dark);font-size:14px}
.products-photo{position:absolute;top:49px;left:0;width:447px;height:305px;
  background:
    linear-gradient(180deg,transparent 55%,rgba(150,146,140,.35) 85%,rgba(120,116,110,.5) 100%),
    linear-gradient(90deg,#5a4e46 0%,#6d6058 9%,#e6e6e3 12%,#f1f1ee 28%,#dcdcd9 33%,#f4f4f2 37%,#eaeae7 62%,#6a5d55 68%,#e2e2df 73%,#ededeb 100%)}
.products-photo svg{position:absolute;inset:0}

.testi-h{top:520px;left:516px}
.testi{top:552px;left:516px;width:257px;height:133px;background:var(--panel);border:1px solid var(--panel-edge)}
.testi-title{position:absolute;top:15px;left:6px;font-size:10.5px;color:var(--purple)}
.testi-text{position:absolute;top:30px;left:6px;width:172px;font-size:8px;line-height:10px;letter-spacing:.3px;color:var(--dark)}
.testi-photo{position:absolute;top:20px;left:174px;width:77px;height:93px;border:1px solid var(--photo-edge);background:linear-gradient(160deg,#8a6a4a,#caa082 55%,#9a8e88)}
.testi .more{position:absolute;top:111px;left:103px}

.enquiry-h{top:695px;left:516px}
.enquiry{top:725px;left:516px;width:257px;height:153px;background:var(--panel);border:1px solid var(--panel-edge)}
.enquiry label{position:absolute;left:12px;font-size:10px;color:var(--label);letter-spacing:.4px}
.enquiry .field{position:absolute;left:78px;width:171px;height:17px;background:var(--field)}
.send{position:absolute;top:125px;left:205px;width:43px;height:21px;border-radius:4px;background:linear-gradient(#fbeff0,#e6c8cc);box-shadow:0 1px 2px rgba(0,0,0,.25);font-size:9px;color:#8a7a7a;text-align:center;line-height:21px;letter-spacing:.5px}

.pay-h{top:887px;left:515px}
.card{position:absolute;left:560px;width:140px;text-align:center;font-size:15px;color:var(--nav-text)}

.call{top:1037px;left:581px;font-size:15px;line-height:16.2px;color:var(--dark)}
.call .phone{color:var(--phone)}

.footer{top:1179px;left:0;width:826px;text-align:center;font-size:9px;color:var(--dark);letter-spacing:.3px}
</style>
</head>
<body>
<div class="abs social"><span><i></i>Friendsy</span><span><i></i>Chirper</span></div>

<div class="abs brand"><i></i>Cradle Lane</div>

<nav class="abs nav">
  <a class="active" href="#">HOME</a>
  <a href="#" style="left:194px">ABOUT US</a>
  <a href="#" style="left:299px">GALLERY</a>
  <a href="#" style="left:403px">SERVICES</a>
  <a href="#" style="left:514px">CONTACTS</a>
</nav>

<div class="abs hero-frame">
  <div class="hero" role="img" aria-label="Soft pink nursery room with white wardrobe, dresser and cot, framed by a leafy green vine border"></div>
</div>

<h2 class="welcome-h">Welcome To Our Site</h2>
<p class="abs welcome-p">Lorem ipsum dolor sit amet, consectetuer adipiscing elit. Aenean commodo ligula eget dolor. Aenean massa. Cum sociis natoque penatibus et magnis dis parturient montes, nascetur ridiculus mus. Donec quam felis, ultricies nec, pellentesque eu, pretium quis, sem. Nulla consequat massa quis enim. Donec pede justo, fringilla vel, aliquet nec, vulputate eget, arcu. In enim justo, rhoncus ut, imperdiet a, venenatis vitae, justo. Nullam dictum felis eu pede mollis pretium. Integer tincidunt. Cras dapibus. Vivamus elementum semper nisi. Aenean vulputate eleifend tellus. Aenean leo ligula, porttitor eu, consequat vitae, eleifend ac, enim. Aliquam lorem ante, dapibus in, viverra quis, feugiat a, tellus. Phasellus viverra nulla ut metus varius laoreet. Quisque rutrum. Aenean imperdiet.</p>
<span class="abs more welcome-more">READ MORE!</span>

<h2 class="products-h">Popular Products</h2>
<section class="abs products">
  <div class="tab" style="left:57px">Item 1</div>
  <div class="tab" style="left:139px">Item 1</div>
  <div class="tab" style="left:219px">Item 1</div>
  <div class="tab" style="left:299px">Item 1</div>
  <div class="products-photo" role="img" aria-label="White nursery furniture: chest of drawers, wardrobe and cot in a tiled product grid">
    <svg width="447" height="305" viewBox="0 0 447 305">
      <g stroke="#fff" stroke-width="2">
        <line x1="145" y1="0" x2="145" y2="305"/>
        <line x1="296" y1="0" x2="296" y2="305"/>
        <line x1="0" y1="154" x2="447" y2="154"/>
      </g>
    </svg>
  </div>
</section>

<h2 class="testi-h">Testimonials</h2>
<section class="abs testi">
  <div class="testi-title">Lorem ipsum dolor</div>
  <p class="testi-text">Lorem ipsum dolor sit amet, consectetuer adipiscing elit. Aenean commodo ligula eget dolor. Aenean massa. Cum sociis natoque penatibus et magnis dis parturient montes, nascetur ridiculus mus.</p>
  <div class="testi-photo" role="img" aria-label="Photo of a smiling mother holding her newborn"></div>
  <span class="more">READ MORE!</span>
</section>

<h2 class="enquiry-h">Quick Enquiry</h2>
<form class="abs enquiry">
  <label style="top:10px">Name *</label><div class="field" style="top:7px"></div>
  <label style="top:38px">Contact no*</label><div class="field" style="top:32px"></div>
  <label style="top:66px">E-mail</label><div class="field" style="top:57px"></div>
  <label style="top:94px">Message</label><div class="field" style="top:79px;height:41px"></div>
  <div class="send">SEND</div>
</form>

<h2 class="pay-h">Payment Option</h2>
<div class="card" style="top:929px">Vireo Pay</div>
<div class="card" style="top:973px">Meridian Card</div>

<div class="abs call">
  Call Us Now<br>
  <span class="phone">1-0061-8XXXXXXXXXXX</span><br>
  Lorem ipsum dolor,<br>
  Quisque Phasellus<br>
  Australia
</div>

<div class="abs footer">Copyright © 2012 Cradle Lane. All rights reserved</div>
</body>
</html>
```